Copper Moth Drift - Blues/Rock band needs a CD cover

Hello there!

We need an amazing artwork for our band's upcoming EP release! This is the launch of our band so it really needs to grab attention, be instantly identifiable and unique!

The band is called: Copper Moth Drift and the album title is Duchess Heron (title of one song).
The music is a Blues/Rock with 2 guitars, drum & bass and a smokey & soulful female voice.
Lyrical themes of the album are: addiction, alcoholism, mistrust, obsession, rejection, murder, and also transcendence.

You can get an idea of the music from http://coppermothdrift-band.example/music/ (please do not get inspiration from the green website banner)

Packaging:
We need an album cover and design of all images for a 4 panel cardboard CD package (Front / Back + 2 Insides) - Digifile Standard size - 141mm x 125mm x 4mm.

Artwork:
Front cover: Artwork + Band name + Album Title
Back Cover: Artwork + Track list (6 song places) + barcode + website/contacts
Inside panels: Artwork + Production / Credits
CD itself

Songs:
Duchess Heron (3.43)
Gentle Stranger (3.33)
Gambler by Night (3.37)
Sinking in the Garden (5.30)
Backdraft (4.01)
Careless Vows (4.34)

Band:
Margaux Vérillon - Vocals
Ned Pickersgill - Guitars, Vocals
Enzo Farnetti - Guitars
Udo Kästlinger - Drums, Percussion
Gaspard Wyss - Bass

All songs by Ned Pickersgill
except “Careless Vows “ by Ned Pickersgill & Enzo Farnetti and “Gambler by Night” By Ned Pickersgill & Gaspard Wyss

Recorded at Rheinquai Tonwerk Studios, Switzerland, Winter 2014/15
Produced and engineered by Luca Fenton and Gareth Mullick @ Q9 Echoworks, Minneapolis, USA
Assistant Engineer

Backing vocals on Gentle Stranger by Rhonda Lisle
Additional Keyboards by Trent Wexley
Artwork by

We want to leave the design open to interpretation just bear in mind this lyrics are really blues oriented, with deep feelings.
We envision a continuity between the panels (in other words telling a story throughout the 4 panels) but this is not a must.
Also, even though we are not looking for a joyful design, it should NOT trigger anxiety or be too dark minded.

We prefer digital graphic or photographic style over illustrative style (for example absolutely no fantasy/airbrush designs) and we do not want anything too literal.

It can be linked to our band name or album title (but please avoid the traditional relaxing black cat or coyote in a Tiara ;-)). It also can have nothing to do with either if them.

With all this said, we are very open to all ideas and want you to think of this as something you can get creative with.

We do not have special fonts for the band name. Let your inspiration flow!
The art will be printed and posted on digital media like itunes amazon.

If you win the contest, you will need to provide files that allow us to alter some of the text (like the track list / production info...) or to update the barcode because this will be available / decided later.

The winner will get high chances to produce other merchandising design projects.

We look forward to your proposals!
Have fun and good luck!

Copper Moth Drift

Target Market(s)

Rock blues amateurs - But not only purist

Requirements
Must have
• Reflect the spirit of the songs
• Have a human element since the person's feeling at the core of our songs
• We should be able to use the artwork on the cd itself.
Nice to have
• Be able to use your band name design as a logo
Should not have
• No relaxing black cat or coyote in a Tiara
• no fantasy/airbrush designs

```html
<!DOCTYPE html>
<html lang="en">
<head>
<meta charset="utf-8">
<title>Copper Moth Drift – Duchess Heron</title>
<link rel="stylesheet" href="https://fonts.googleapis.com/css2?family=Tinos:ital@0;1&display=swap">
<style>
  :root {
    --page: #ffffff;
    --ink: #1c1c1c;
    --spine: #0d0d0d;
    --spine-text: #f2f2f2;
    --tile-light: #d9d9d7;
    --tile-dark: #3a3a3a;
    --label-card: #ecebe8;
    --wall: #e6e6e4;
    --wall-shade: #cfcfcc;
    --floor: #2a2a2a;
    --floor-deep: #050505;
    --cover-text: #f4f4f4;
  }
  * { margin: 0; padding: 0; box-sizing: border-box; }
  html, body {
    width: 1200px;
    height: 525px;
    overflow: hidden;
    background: var(--page);
  }
  .spread {
    position: relative;
    width: 1200px;
    height: 525px;
    font-family: "Tinos", "Times New Roman", serif;
    color: var(--ink);
  }

  /* Back cover */
  .back-cover {
    position: absolute;
    left: 0;
    top: 0;
    width: 586px;
    height: 525px;
  }
  .back-artwork {
    position: absolute;
    inset: 0;
    background:
      linear-gradient(135deg, var(--tile-dark) 0%, var(--tile-light) 25%, var(--tile-dark) 50%, var(--tile-light) 75%, var(--tile-dark) 100%);
  }
  .tracklist-card {
    position: absolute;
    left: 148px;
    top: 128px;
    width: 303px;
    height: 307px;
    background: var(--label-card);
    text-align: center;
  }
  .tracklist {
    list-style: none;
    margin-top: 75px;
    font-style: italic;
    font-size: 13px;
    line-height: 26px;
  }
  .website {
    position: absolute;
    left: 0;
    right: 0;
    bottom: 8px;
    font-size: 13px;
  }

  /* Spine */
  .spine {
    position: absolute;
    left: 586px;
    top: 0;
    width: 24px;
    height: 525px;
    background: var(--spine);
    color: var(--spine-text);
  }
  .spine-text {
    position: absolute;
    left: 50%;
    writing-mode: vertical-rl;
    transform: translateX(-50%);
    font-size: 10px;
    letter-spacing: 1.6px;
  }
  .spine-band { top: 14px; text-transform: uppercase; }
  .spine-title { bottom: 14px; letter-spacing: 2.4px; }

  /* Front cover */
  .front-cover {
    position: absolute;
    left: 648px;
    top: 45px;
    width: 510px;
    height: 430px;
    overflow: hidden;
  }
  .front-artwork {
    position: absolute;
    inset: 0;
    background: linear-gradient(180deg,
      var(--wall) 0%, var(--wall-shade) 68%,
      var(--floor) 70%, var(--floor-deep) 100%);
  }
  .album-title {
    position: absolute;
    top: 84px;
    left: 0;
    right: 0;
    text-align: center;
    font-style: italic;
    font-weight: 400;
    font-size: 22px;
    letter-spacing: 4px;
  }
  .band-name {
    position: absolute;
    top: 365px;
    left: 0;
    right: 0;
    text-align: center;
    font-weight: 400;
    font-size: 16px;
    letter-spacing: 2.5px;
    text-transform: uppercase;
    color: var(--cover-text);
  }
</style>
</head>
<body>
<main class="spread">

  <section class="back-cover">
    <div class="back-artwork" role="img" aria-label="Black and white photograph of chevron-striped floor tiles framing the track list"></div>
    <div class="tracklist-card">
      <ol class="tracklist">
        <li>duchess heron (3.43)</li>
        <li>gentle stranger (3.33)</li>
        <li>gambler by night (3.37)</li>
        <li>sinking in the garden (5.30)</li>
        <li>backdraft (4.01)</li>
        <li>careless vows (4.34)</li>
      </ol>
      <p class="website">www.coppermothdrift.example</p>
    </div>
  </section>

  <aside class="spine">
    <span class="spine-text spine-band">Copper Moth Drift</span>
    <span class="spine-text spine-title">duchess heron</span>
  </aside>

  <section class="front-cover">
    <div class="front-artwork" role="img" aria-label="Black and white photograph of a pale weathered wall meeting a dark paved floor"></div>
    <h1 class="album-title">duchess heron</h1>
    <h2 class="band-name">Copper Moth Drift</h2>
  </section>

</main>
</body>
</html>
```